New Company Brochure for Email send out

Want to have a new professional and eye catching company brochure
We are an I.T. Infrastructure solution provider

Focus Solution
1) Server Room Setup (UPS, CRAC, etc)
2) All-in-One Rack Solution (Key focus)
3) Structured Cabling and Fiber Backbone wiring
4) other solution (CCTV & Access Control Solution, Conference Room AV Solution)

Hope to have
1) total around 6 pages (including front cover and last page)
2) Suggested format : Powerpoint, word, excel or visio
3) sorry we have no knowledge on AI
Updates

Low design quality

Target Market(s)

Enterprise

Industry/Entity Type

I.T.

Requirements
Must have
• Our Product Photo (All-in-One Rack Solution, Structured Cabling, Server room Setup)
Nice to have
• Some our vendor partners logo
Should not have
• Our Existing Client Logo

```html
<!DOCTYPE html>
<html lang="en">
<head>
<meta charset="utf-8">
<title>Vantor Technology – CCTV &amp; Conference Room Solutions</title>
<link href="https://fonts.googleapis.com/css2?family=Open+Sans:wght@400;600;700;800&display=swap" rel="stylesheet">
<style>
  :root{
    --teal:#17a993;
    --blue:#1b5aa6;
    --text:#555a5e;
    --paper:#ffffff;
    --muted:#8a8f93;
  }
  *{box-sizing:border-box;margin:0;padding:0}
  html,body{width:1200px;height:848px;overflow:hidden;background:var(--paper)}
  body{position:relative;font-family:"Open Sans",Arial,sans-serif;color:var(--text)}
  .hero{position:absolute;left:0;top:0;width:1200px;height:303px}
  .section{position:absolute;top:340px;width:536px}
  .section--cctv{left:37px}
  .section--av{left:634px;width:517px}
  .section__title{
    font-family:"Open Sans",Arial,sans-serif;font-weight:800;
    font-size:31px;letter-spacing:-1.6px;color:var(--teal);
    line-height:40px;white-space:nowrap;
  }
  .section__body{margin-top:37px;font-size:11.9px;letter-spacing:-0.15px;line-height:14.6px;text-align:justify;hyphens:manual}
  .section--av .section__body{margin-top:33px}
  .section__body p+p{margin-top:14.6px}
  .section__lead{margin-top:14.6px;font-size:11.9px;letter-spacing:-0.1px}
  .brand{font-weight:700;color:var(--blue)}
  .features{list-style:none;margin-top:14px}
  .section--av .features{margin-top:32px}
  .features li{position:relative;padding-left:23px;font-size:11.9px;letter-spacing:-0.1px;height:29px;line-height:14px;white-space:nowrap}
  .features li::before{
    content:"";position:absolute;left:0;top:2px;width:10px;height:10px;
    border-radius:50%;background:var(--teal);
  }
  .product{position:absolute;border-radius:14px}
  .product--cameras{left:270px;top:604px;width:306px;height:166px;
    background:radial-gradient(ellipse at 50% 50%,#e9ebec 0%,#d4d7d9 60%,#f4f5f6 100%)}
  .product--conference{left:922px;top:564px;width:230px;height:220px;
    background:radial-gradient(ellipse at 50% 50%,#dcdee0 0%,#c8cbce 55%,#f2f3f4 100%)}
  .page-number{position:absolute;top:816px;font-size:10px;color:var(--muted)}
  .page-number--left{left:570px}
  .page-number--right{left:1165px}
</style>
</head>
<body>
  <svg class="hero" viewBox="0 0 1200 303" xmlns="http://www.w3.org/2000/svg">
    <defs>
      <linearGradient id="lockTone" x1="0" x2="1" y1="0" y2="0">
        <stop offset="0" stop-color="#e9e9ea"/>
        <stop offset="0.2" stop-color="#ee5a3c"/>
        <stop offset="0.35" stop-color="#f1efee"/>
        <stop offset="0.5" stop-color="#5c8fa7"/>
        <stop offset="0.62" stop-color="#9c8660"/>
        <stop offset="0.8" stop-color="#d8d9da"/>
        <stop offset="1" stop-color="#c9cacb"/>
      </linearGradient>
      <linearGradient id="roomTone" x1="0" x2="1" y1="0" y2="1">
        <stop offset="0" stop-color="#d6dada"/>
        <stop offset="0.5" stop-color="#eef0f1"/>
        <stop offset="1" stop-color="#8a8d90"/>
      </linearGradient>
    </defs>
    <path d="M0 0H1200V262Q1200 302 1160 302H40Q0 302 0 262Z" fill="var(--teal)"/>
    <path d="M600 50Q600 0 650 0H1200V16H600Z" fill="var(--blue)"/>
    <path d="M0 16H580Q600 16 600 40V287H40Q0 287 0 247Z" fill="url(#lockTone)" role="img" aria-label="Close-up photo of a padlock on a painted metal door"/>
    <path d="M601 287V60Q601 16 645 16H1200V247Q1200 287 1160 287Z" fill="url(#roomTone)" role="img" aria-label="Photo of a glass-walled conference room with a long white table and wall display"/>
  </svg>

  <section class="section section--cctv">
    <h2 class="section__title">CCTV &amp; ACCESS CONTROL SOLUTION</h2>
    <div class="section__body">
      <p>Vantor design and implement access control solutions that fits office facilities and restricted areas like data center. Advanced technologies bring you the functionality you need with expand&shy;ability for the future.</p>
      <p>With multiple combination of use of means of access, cards, finger-prints and facial recognition; organisations not only can monitor attendance but only ensure the highest level of security for special areas. No worries for multiple offices! We can tie them together to ease and automate the overall management.</p>
    </div>
    <p class="section__lead"><span class="brand">VANTOR</span>’s solution in Access Control covers</p>
    <ul class="features">
      <li>Two or more factor authentications</li>
      <li>Card identification</li>
      <li>Password identification</li>
      <li>Fingerprint identification</li>
      <li>Facial identifcation</li>
    </ul>
  </section>

  <div class="product product--cameras" role="img" aria-label="Product photo of dome and bullet security cameras"></div>

  <section class="section section--av">
    <h2 class="section__title">CONFERENCE ROOM AV SOLUTION</h2>
    <div class="section__body">
      <p>Conference Room is a place putting together multimedia presentation technology, video and audio conferencing systems, interactive communication products and centralised integrated management systems. Vantor Technology as a leading IT &amp; AV system integrator offers a wide range of different audiovisual solutions based on your need. With our field engineer’s exten&shy;sive knowledge in not only AV, but also network and IP, overall project is simplified and pro&shy;ject life cycle are well shortened.</p>
    </div>
    <p class="section__lead"><span class="brand">VANTOR’</span>s solution in Audiovisual &amp; Conferencing covers</p>
    <ul class="features">
      <li>Video Conferencing System</li>
      <li>Telepresence</li>
      <li>Conference Room Centralised Control System</li>
      <li>Interactive Presentation Tools</li>
    </ul>
  </section>

  <div class="product product--conference" role="img" aria-label="Product photo of a video conferencing camera, codec unit, speakerphone and remote"></div>

  <span class="page-number page-number--left">04</span>
  <span class="page-number page-number--right">05</span>
</body>
</html>
```